Business Card Design for Photographer

Updating business card design. Must use included logo. We're a luxury wedding photography business. Elegancy, luxury, consistency are messages we wish to convey.

Visit our website at www.colbyvarnway.com to familiarize yourself more with our brand design currently (fonts, colors etc.). This is what we want to maintain.

Target Market(s)

Luxury Brides and Grooms

Industry/Entity Type

Wedding

Contact Information for Business Card

Current logo (attached to brief)
Name: Colby Varnway
Phone: 5208813047
website/blog
Email

Requirements
Must have
• Current logo (attached to brief)
• Name: Colby Varnway
• Phone: 5208813047
• website/blog
• Email
• Instagram username
Should not have
• bright colors, fonts that don't suit our brand (visit www.colbyvarnway.com)

```html
<!DOCTYPE html>
<html lang="en">
<head>
<meta charset="utf-8">
<title>Colby Varnway Photographers – Identity Sheet</title>
<link rel="stylesheet" href="https://fonts.googleapis.com/css2?family=Lato:wght@400&display=swap">
<style>
  :root {
    --paper: #ffffff;
    --slate: #6b7474;
    --ink: #141414;
    --card-black: #000000;
    --rule: #8a8f8f;
    --shadow: rgba(0, 0, 0, 0.55);
  }
  html, body {
    margin: 0;
    padding: 0;
    overflow: hidden;
  }
  body {
    width: 857px;
    height: 1200px;
    background: var(--paper);
    position: relative;
    font-family: "Lato", "Gill Sans", sans-serif;
    font-weight: 400;
  }
  .sheet-rule {
    position: absolute;
    left: 149px;
    top: 0;
    width: 1px;
    height: 1200px;
    background: var(--rule);
  }
  .mark-square {
    position: absolute;
    background: var(--slate);
  }
  .sheet-mark { left: 13px; top: 13px; width: 124px; height: 124px; }

  .wordmark {
    position: absolute;
    text-align: center;
    color: var(--slate);
    text-transform: uppercase;
    line-height: 1;
  }
  .sheet-wordmark { left: 150px; width: 666px; top: 34px; }
  .wordmark .name { display: block; letter-spacing: 0.14em; }
  .wordmark .trade { display: block; letter-spacing: 0.38em; }
  .sheet-wordmark .name { font-size: 40px; }
  .sheet-wordmark .trade { font-size: 19px; margin-top: 20px; }

  .card {
    position: absolute;
    width: 601px;
    height: 343px;
    box-shadow: 9px 9px 7px var(--shadow);
  }
  .card-front { left: 182px; top: 287px; background: var(--card-black); }
  .card-front .mark-square { left: 245px; top: 116px; width: 115px; height: 114px; }
  .card-front .front-name {
    position: absolute; left: 0; width: 100%; top: 238px;
    text-align: center; color: var(--slate); font-size: 15px; letter-spacing: 0.2em;
    text-transform: uppercase;
  }
  .card-front .front-url {
    position: absolute; left: 0; width: 100%; top: 301px;
    text-align: center; color: var(--paper); font-size: 24px;
  }

  .card-back { left: 218px; top: 694px; background: var(--paper); box-shadow: 9px 9px 7px var(--shadow), 0 0 1px rgba(0,0,0,0.25); }
  .card-back .card-rule { position: absolute; left: 89px; top: 0; width: 1px; height: 100%; background: var(--rule); }
  .card-back .mark-square { left: 7px; top: 9px; width: 75px; height: 76px; }
  .card-back .wordmark { left: 89px; width: 512px; top: 21px; }
  .card-back .wordmark .name { font-size: 25px; }
  .card-back .wordmark .trade { font-size: 13px; margin-top: 13px; }

  .contact { position: absolute; left: 172px; top: 164px; color: var(--ink); }
  .contact .person { font-size: 24px; margin: 0 0 14px; font-weight: 400; }
  .contact ul { list-style: none; margin: 0; padding: 0; font-size: 18px; line-height: 24.5px; }
</style>
</head>
<body>
  <div class="sheet-rule"></div>
  <div class="mark-square sheet-mark"></div>
  <div class="wordmark sheet-wordmark">
    <span class="name">Colby Varnway</span>
    <span class="trade">Photographers</span>
  </div>

  <section class="card card-front">
    <div class="mark-square"></div>
    <div class="front-name">Colby Varnway</div>
    <div class="front-url">www.colbyvarnway.com</div>
  </section>

  <section class="card card-back">
    <div class="mark-square"></div>
    <div class="card-rule"></div>
    <div class="wordmark">
      <span class="name">Colby Varnway</span>
      <span class="trade">Photographers</span>
    </div>
    <div class="contact">
      <h2 class="person">Colby Varnway</h2>
      <ul>
        <li>5208813047</li>
        <li>colby@colbyvarnway.com</li>
        <li>www.colbyvarnway.com/blog</li>
        <li>instagram/colbyvarnwayphoto</li>
      </ul>
    </div>
  </section>
</body>
</html>
```